tovrin company need business card, envelope and letterhead design

Check on the attached file wherein you can find our logo and information about the company
Business card will double sided English version and Arabic version

Industry/Entity Type

Business

Requirements
Must have
• include the design also for the letterhead and envelop
Nice to have

```html
<!DOCTYPE html>
<html lang="en">
<head>
<meta charset="utf-8">
<title>Tovrin Stationery</title>
<link href="https://fonts.googleapis.com/css2?family=Quicksand:wght@400;500;600;700&display=swap" rel="stylesheet">
<style>
:root{
  --bg:#0b0b0b;
  --paper:#ffffff;
  --band:#ececec;
  --band-soft:#f3f3f3;
  --blue:#1d72c2;
  --steel:#8a8a8a;
  --ink:#333333;
  --muted:#777777;
}
*{box-sizing:border-box;margin:0;padding:0}
html,body{width:1200px;height:1020px;overflow:hidden;background:var(--bg)}
body{font-family:"Quicksand",sans-serif;color:var(--ink);position:relative}
.sheet{position:absolute;background:var(--paper);overflow:hidden}
.sheet svg.shape{position:absolute;left:0;width:100%}
.wordmark{position:absolute;display:flex;align-items:center;gap:6px;color:var(--blue);font-weight:700;letter-spacing:2px}
.wordmark .dot{width:10px;height:10px;background:var(--blue)}
.header-art{position:absolute;top:0;background:linear-gradient(90deg,#c9dcef 0%,#dcdcdc 100%)}
.footer-art{position:absolute;left:0;bottom:0;background:linear-gradient(180deg,#e4e4e4,#d8d8d8)}
.contact{position:absolute;display:flex;align-items:center;gap:10px;font-size:6.5px;color:var(--muted);line-height:1.35}
.contact .addr{text-align:right}
.contact svg{width:9px;height:9px;fill:var(--blue);flex:none}

/* letterhead */
.letterhead{left:40px;top:120px;width:500px;height:707px}
.letterhead .wordmark{left:52px;top:130px;font-size:22px}
.recipient{position:absolute;left:52px;top:190px;font-size:8.5px;line-height:1.4;color:var(--ink)}
.recipient strong{font-weight:600}
.letter-body{position:absolute;left:52px;top:240px;width:396px;font-size:7.5px;line-height:1.55;color:#555}
.letter-body p{text-indent:24px;margin-bottom:10px;text-align:justify}
.signoff{position:absolute;left:52px;top:470px;font-size:8px;color:var(--muted)}
.signature{position:absolute;left:52px;top:530px;font-size:10px;font-weight:600;color:var(--ink)}
.signature small{display:block;font-size:7.5px;font-weight:400;color:var(--muted)}
.letterhead .contact{right:36px;bottom:34px}

/* business cards */
.card{top:60px;width:280px;height:160px}
.card-front{left:580px}
.card-front .wordmark{left:26px;top:90px;font-size:15px}
.card-back{left:880px}
.card-back .person{position:absolute;left:20px;top:32px;font-size:9px;font-weight:600;color:var(--ink)}
.card-back .person b{color:var(--blue);font-weight:700}
.card-back .person small{display:block;font-size:5.5px;font-weight:400;color:var(--muted)}
.card-back .details{position:absolute;right:18px;top:28px;font-size:5px;line-height:1.5;color:var(--muted);text-align:right}

/* envelopes */
.envelope{left:580px;width:580px;height:290px}
.envelope-back{top:250px}
.envelope-back .flap{position:absolute;left:0;top:0;width:100%;height:150px}
.envelope-back .contact{right:30px;bottom:100px}
.envelope-front{top:570px}
.envelope-front .wordmark{left:44px;top:140px;font-size:20px}
.envelope-front .sender{position:absolute;left:44px;top:172px;font-size:7.5px;line-height:1.45;color:var(--muted)}
</style>
</head>
<body>

<!-- Letterhead -->
<section class="sheet letterhead" aria-label="Letterhead">
  <svg class="shape" style="top:0;height:110px" viewBox="0 0 500 110" preserveAspectRatio="none">
    <rect width="500" height="110" fill="var(--band)"/>
    <path d="M0 110 V100 H250 C285 100 285 78 320 78 H500 V110 Z" fill="var(--paper)"/>
  </svg>
  <div class="header-art" style="left:318px;width:140px;height:72px" role="img" aria-label="Brand header graphic in blue and grey"></div>
  <div class="wordmark"><span class="dot"></span>TOVRIN</div>

  <div class="recipient"><strong>Mira Castell</strong><br>12 Harbour Lane,<br>Singapore 408177</div>

  <div class="letter-body">
    <p>Lorem ipsum dolor sit amet, consectetur adipiscing elit. Suspendisse condimentum egestas tellus et viverra. Vestibulum euismod lacus eget nisi ornare, id laoreet tortor dapibus. Donec lacinia euismod diam, condimentum tempus risus. Ut et felis tempor eros blandit feugiat ut non enim. In vestibulum ligula blandit magna blandit dictum. Sed malesuada erat id mauris pretium, eu congue felis interdum. Aenean ultricies enim nec lorem vestibulum, nec commodo quam sagittis. Cras bibendum mauris eget aliquet semper. Libero ipsum ultricies nunc, euismod pellentesque orci risus amet nibh. Maecenas feugiat mi a metus convallis pharetra.</p>
    <p>Duis porta turpis ut pulvinar hendrerit elit lorem lobortis turpis, lacinia semper purus nisi ac nisi. Sed consectetur ante scelerisque tortor pellentesque imperdiet. Pellentesque habitant morbi tristique senectus et netus et malesuada fames ac turpis egestas. Quisque justo turpis, varius ante nec, tincidunt pharetra tellus. Donec non euismod est. Nulla in elit quis tellus mattis feugiat vitae ut magna. Etiam at nisi quis dolor facilisis hendrerit placerat et risus. Vestibulum ac sapien ut justo varius venenatis.</p>
    <p>Donec eget nunc bibendum, sodales augue vel, dapibus nibh. Pellentesque habitant morbi tristique senectus et netus et malesuada fames ac turpis egestas. Quisque justo turpis, varius ante nec, accumsan ultricies magna. Mauris lorem lectus, dignissim nec felis a, tincidunt pharetra tellus. Donec non euismod est. Mauris vitae orci augue. Duis sit amet erat id lectus.</p>
  </div>

  <div class="signoff">Regards</div>
  <div class="signature">Daniel Reyes<small>Executive Director</small></div>

  <svg class="shape" style="bottom:0;height:110px" viewBox="0 0 500 110" preserveAspectRatio="none">
    <path d="M0 30 H170 C205 30 205 10 240 10 H500 V110 H0 Z" fill="var(--band-soft)"/>
  </svg>
  <div class="footer-art" style="width:200px;height:80px" role="img" aria-label="Faint brand decoration in light grey"></div>
  <div class="contact">
    <div class="addr">Nakheel Crest Road<br>Al Wurud<br>P.O. Box 4412-30918<br>Kingdom of Saudi Arabia</div>
    <svg viewBox="0 0 10 10"><path d="M5 0a3.5 3.5 0 0 0-3.5 3.5C1.5 6 5 10 5 10s3.5-4 3.5-6.5A3.5 3.5 0 0 0 5 0zm0 5a1.5 1.5 0 1 1 0-3 1.5 1.5 0 0 1 0 3z"/></svg>
    <div>tovrin.sa@mailhub.com</div>
    <svg viewBox="0 0 10 10"><path d="M4 6l2-2M3.5 4.5l-1 1a1.6 1.6 0 0 0 2 2l1-1M6.5 5.5l1-1a1.6 1.6 0 0 0-2-2l-1 1" stroke="var(--blue)" stroke-width="1.2" fill="none"/></svg>
    <div>T. 011 7302264<br>F. 011 7302 265</div>
    <svg viewBox="0 0 10 10"><path d="M2.3 0.8l1.6 2.2-1 1.1a6 6 0 0 0 3 3l1.1-1 2.2 1.6-.9 1.6C5 9 1 5 .7 1.7z"/></svg>
  </div>
</section>

<!-- Business card front -->
<section class="sheet card card-front" aria-label="Business card, front">
  <svg class="shape" style="top:0;height:70px" viewBox="0 0 280 70" preserveAspectRatio="none">
    <rect width="280" height="70" fill="var(--band)"/>
    <path d="M0 70 V62 H120 C140 62 140 46 160 46 H280 V70 Z" fill="var(--paper)"/>
  </svg>
  <div class="header-art" style="left:160px;width:78px;height:40px" role="img" aria-label="Brand header graphic in blue and grey"></div>
  <div class="wordmark"><span class="dot" style="width:7px;height:7px"></span>TOVRIN</div>
</section>

<!-- Business card back -->
<section class="sheet card card-back" aria-label="Business card, back">
  <div class="person">Faris Bin Omar <b>Al Harithi</b><small>Managing Director, Tovrin Trading</small></div>
  <div class="details">Nakheel Crest Road<br>Al Wurud, Riyadh<br>T. 011 7302264<br>tovrin.sa@mailhub.com</div>
  <svg class="shape" style="bottom:0;height:70px" viewBox="0 0 280 70" preserveAspectRatio="none">
    <path d="M0 22 H110 C130 22 130 8 150 8 H280 V70 H0 Z" fill="var(--band-soft)"/>
  </svg>
  <div class="footer-art" style="width:110px;height:52px" role="img" aria-label="Faint brand decoration in light grey"></div>
</section>

<!-- Envelope back -->
<section class="sheet envelope envelope-back" aria-label="Envelope, back">
  <svg class="flap" viewBox="0 0 580 150" preserveAspectRatio="none">
    <path d="M0 0 H580 L320 140 Q290 154 260 140 Z" fill="#fbfafa" stroke="#e2e2e2" stroke-width="1"/>
  </svg>
  <svg class="shape" style="bottom:0;height:130px" viewBox="0 0 580 130" preserveAspectRatio="none">
    <path d="M0 40 H190 C225 40 225 18 260 18 H580 V130 H0 Z" fill="var(--band-soft)"/>
  </svg>
  <div class="footer-art" style="width:220px;height:100px" role="img" aria-label="Faint brand decoration in light grey"></div>
  <div class="contact">
    <div class="addr">Nakheel Crest Road<br>Al Wurud<br>P.O. Box 4412-30918<br>Kingdom of Saudi Arabia</div>
    <svg viewBox="0 0 10 10"><path d="M5 0a3.5 3.5 0 0 0-3.5 3.5C1.5 6 5 10 5 10s3.5-4 3.5-6.5A3.5 3.5 0 0 0 5 0zm0 5a1.5 1.5 0 1 1 0-3 1.5 1.5 0 0 1 0 3z"/></svg>
    <div>tovrin.sa@mailhub.com</div>
    <svg viewBox="0 0 10 10"><path d="M4 6l2-2M3.5 4.5l-1 1a1.6 1.6 0 0 0 2 2l1-1M6.5 5.5l1-1a1.6 1.6 0 0 0-2-2l-1 1" stroke="var(--blue)" stroke-width="1.2" fill="none"/></svg>
    <div>T. 011 7302264<br>F. 011 7302 265</div>
    <svg viewBox="0 0 10 10"><path d="M2.3 0.8l1.6 2.2-1 1.1a6 6 0 0 0 3 3l1.1-1 2.2 1.6-.9 1.6C5 9 1 5 .7 1.7z"/></svg>
  </div>
</section>

<!-- Envelope front -->
<section class="sheet envelope envelope-front" aria-label="Envelope, front">
  <svg class="shape" style="top:0;height:120px" viewBox="0 0 580 120" preserveAspectRatio="none">
    <rect width="580" height="120" fill="var(--band)"/>
    <path d="M0 120 V110 H300 C335 110 335 86 370 86 H580 V120 Z" fill="var(--paper)"/>
  </svg>
  <div class="header-art" style="left:330px;width:148px;height:78px" role="img" aria-label="Brand header graphic in blue and grey"></div>
  <div class="wordmark"><span class="dot"></span>TOVRIN</div>
  <div class="sender">Nakheel Crest Road, Al Wurud<br>P.O. Box 4412-30918<br>Kingdom of Saudi Arabia</div>
</section>

</body>
</html>
```